Heron Trade finance web design

We are a newly established business which provides invoice finance to Small Businesses in England and Wales.
Our approach is very much a funder where the small business owner can talk to the decision maker. We will guarantee on receipt of information, a decision within 24 hours.
We are not a bank so the look of the website need to be friendly but professional.
Have two types of people we are trying to attract to the website: 1) partners who are small business owners and 2) introducers who is accountants and commercial brokers who introduce us to the small businesses.
Currently no website, although domain has been reserved.
The design should be:
Professional
“Clean” Look
Designed to convey Trust and Authority.
Appeal to the small business owner.
Must incorporate:
Logo (attached)
Front page:Top tabs to other pages 1) About us 2) Services 3) Introducers 4) Contact us
Need picture and logo on page.
1) About us page- Room for talk about the company, the people and our critera.
2) Services page- We need for what invoice finance is, and 5 boxes for different services we will provide. (link on page to contact us)
3) Introducers page- We need a part for why become an introducer? Who we can help? Why we are different? (link on page to contact us)
4) Contact us page- Office address, email, tel and if possible a map and a contact me part which will email direct to us.
Text will be provided for the design, if we can see the setup of the website we will provide a part for each of the pages to support.
Styles we think convey the correct image:
www.brindlecapital.example
www.tollmarkfs.example
www.qelfunding.example
Small business owners
Finance
5+ page

```html
<!DOCTYPE html>
<html lang="en">
<head>
<meta charset="utf-8">
<title>Heron Trade finance</title>
<link href="https://fonts.googleapis.com/css2?family=Roboto:ital,wght@0,300;0,400;0,500;0,700;1,400&display=swap" rel="stylesheet">
<style>
:root{
  --blue:#29a3dc;
  --ink:#1f232b;
  --text:#5b6270;
  --muted:#8a909b;
  --line:#e3e6ea;
  --nav:#2f3543;
  --footer:#333947;
  --footer-rule:#444b5a;
  --soft:#eef0f4;
  --field:#f2f4f7;
  --brand:#c0272d;
  --white:#ffffff;
}
*{box-sizing:border-box;margin:0;padding:0}
html,body{width:1200px;height:3600px;overflow:hidden;background:var(--white)}
body{font-family:'Roboto',Arial,sans-serif;color:var(--ink);position:relative}
.abs{position:absolute}

/* top bar */
.topbar{top:0;left:0;width:1200px;height:91px;background:var(--white)}
.brand{font-weight:700;color:var(--brand);font-size:23px;letter-spacing:-.2px}
.topbar .brand{left:84px;top:31px}
.info{display:flex;gap:12px;align-items:flex-start;font-size:12.5px;line-height:17px;color:var(--text)}
.info strong{display:block;color:var(--ink);font-weight:500}
.info svg{flex:none;margin-top:2px}

/* nav */
.mainnav{top:91px;left:0;width:1200px;height:55px;background:var(--nav)}
.mainnav ul{list-style:none;display:flex;position:absolute;left:84px;top:0;height:55px;align-items:center}
.mainnav li{font-size:12.5px;font-weight:500;color:var(--white);margin-right:36px;display:flex;align-items:center;gap:6px}
.mainnav li.active{color:var(--blue)}
.mainnav .search{right:92px;top:17px}

/* hero */
.hero{top:146px;left:0;width:1200px;height:524px;background:linear-gradient(90deg,#e9ebee 0%,#f6f6f7 45%,#eceef1 100%);overflow:hidden}
.hero-photo{left:456px;top:0;width:704px;height:524px;background:linear-gradient(100deg,rgba(246,246,247,0) 0%,#d9dde2 30%,#b9bfc7 60%,#e4e6e9 100%)}
.hero h1{left:166px;top:132px;font-size:46px;line-height:56px;font-weight:700;color:#242830;letter-spacing:-.5px}
.btn{display:inline-flex;align-items:center;justify-content:center;font-size:12.5px;font-weight:500}
.btn-primary{background:var(--blue);color:var(--white)}
.btn-outline{border:2px solid #cfd3d8;color:var(--ink);background:rgba(255,255,255,.6)}
.hero .learn{left:166px;top:274px;width:144px;height:43px}
.hero .ours{left:329px;top:274px;width:141px;height:43px}
.slide-arrow{top:243px;width:41px;height:38px;background:#c9cdd3;display:flex;align-items:center;justify-content:center}

/* features */
.feature{top:744px;width:250px;text-align:center}
.feature h3{font-size:17px;font-weight:700;margin-top:34px;color:var(--ink)}
.feature p{font-size:12.5px;line-height:19px;color:var(--muted);margin:16px auto 0;width:205px}
.feature svg{display:block;margin:0 auto}

/* what we do */
.whatwedo{top:1039px;left:0;width:1200px;height:192px;overflow:hidden}
.whatwedo .bg{inset:0;background:linear-gradient(100deg,#5d7d9c 0%,#3f5d7c 35%,#2f4156 70%,#39495c 100%)}
.whatwedo h2{left:82px;top:74px;font-size:36px;font-weight:700;color:var(--white)}
.whatwedo .rule{left:344px;top:84px;width:1px;height:32px;background:rgba(255,255,255,.5)}
.whatwedo p{left:360px;top:86px;font-size:18px;font-weight:300;color:rgba(255,255,255,.9)}
.whatwedo .btn{left:958px;top:77px;width:160px;height:46px}

/* section heads */
.section-title{left:0;width:1200px;text-align:center;font-size:37px;font-weight:700;color:var(--ink)}
.title-rule{left:570px;width:60px;height:4px;background:var(--blue)}

/* about */
.tabs{top:1411px;left:79px;width:507px;height:51px;display:flex;border:1px solid var(--line)}
.tabs span{flex:1;display:flex;align-items:center;justify-content:center;font-size:16px;color:#444a55;border-left:1px solid var(--line)}
.tabs span:first-child{border-left:none;background:var(--blue);color:var(--white)}
.about-intro{top:1491px;left:79px;width:510px;font-size:12.5px;line-height:19px;color:var(--text)}
.stats{top:1566px;left:79px;width:510px;display:flex}
.stat{width:170px;height:84px;border-left:1px solid var(--line);text-align:center}
.stat:first-child{border-left:none}
.stat b{display:block;font-size:48px;font-weight:400;color:var(--blue);line-height:56px}
.stat i{display:block;font-style:normal;font-size:11.5px;color:var(--text);margin-top:6px}
.about-copy{top:1422px;left:677px;width:440px}
.about-copy h3{font-size:18px;font-weight:700;color:var(--ink)}
.about-copy p{font-size:12.5px;line-height:21px;color:var(--text);margin-top:18px}
.about-copy .btn{margin-top:24px;width:127px;height:41px;border:2px solid var(--blue);color:var(--blue);background:var(--white)}

/* funding calculator */
.calc-band{top:1860px;left:0;width:1200px;height:480px;background:var(--soft)}
.calc-photo{top:1769px;left:672px;width:456px;height:571px;background:linear-gradient(180deg,#f3f5f8 0%,#dbe6f1 55%,#9fbcd8 100%)}
.calc-card{top:1776px;left:79px;width:593px;height:624px;background:var(--white);border:1px solid #e6e8ec;box-shadow:0 6px 24px rgba(30,40,60,.08)}
.calc-card h2{position:absolute;left:48px;top:62px;font-size:34px;font-weight:700;color:var(--ink)}
.calc-card .rule{position:absolute;left:48px;top:126px;width:60px;height:4px;background:var(--blue)}
.field{position:absolute;width:238px}
.field label{display:block;font-size:11.5px;color:var(--muted);margin-bottom:8px}
.field .input{height:43px;background:var(--field);font-size:12px;color:#a4a9b2;padding:14px 16px}
.field.total .input{border-bottom:3px solid var(--blue)}
.calc-note{position:absolute;left:48px;top:352px;font-size:11.5px;color:var(--muted)}

/* testimonials */
.quote-card{top:2623px;width:273px;height:291px;background:var(--white);border:1px solid #e6e8ec;box-shadow:0 4px 18px rgba(30,40,60,.06);text-align:center}
.avatar{width:63px;height:63px;border-radius:50%;margin:35px auto 0;background:linear-gradient(160deg,#e6d6c8,#b49a86)}
.quote-card p{font-size:12.5px;line-height:18px;font-style:italic;color:var(--muted);width:205px;margin:26px auto 0}
.quote-card h4{font-size:13px;font-weight:700;margin-top:14px;color:var(--ink)}
.quote-card small{display:block;font-size:11.5px;color:var(--muted);margin-top:6px}
.t-arrow{top:2748px}

/* partners */
.partners{top:2990px;left:0;width:1200px;height:192px;background:#f5f6f8}
.badge{position:absolute;top:48px;height:96px;display:flex;align-items:center;justify-content:center}

/* footer */
.footer{top:3182px;left:0;width:1200px;height:418px;background:var(--footer)}
.footer .brand{left:84px;top:68px;color:var(--white);font-size:21px}
.footer-about{left:79px;top:138px;width:220px;font-size:12.5px;line-height:19px;color:#d9dce2}
.follow{left:79px;top:220px;display:flex;align-items:center;gap:14px;font-size:11.5px;color:#d9dce2}
.follow i{width:22px;height:22px;border-radius:50%;background:var(--white);display:block}
.footer h5{font-size:16px;font-weight:700;color:var(--white)}
.footer .fcol-rule{height:1px;background:var(--footer-rule)}
.links{font-size:11.5px;color:#9aa0ac;line-height:31px}
.contact-icons{left:614px;top:136px;display:flex;flex-direction:column;gap:14px}
.subscribe p{font-size:12px;color:#d9dce2}
.sub-form{display:flex;margin-top:14px}
.sub-form .email{width:177px;height:41px;background:var(--white);font-size:11.5px;color:#a4a9b2;padding:14px 12px}
.sub-form .send{width:65px;height:41px;background:var(--blue);color:var(--white);font-size:12.5px;display:flex;align-items:center;justify-content:center}
.footer .bottom-rule{left:0;top:358px;width:1200px;height:1px;background:var(--footer-rule)}
</style>
</head>
<body>

<header class="abs topbar">
  <div class="abs brand">Heron Trade finance</div>
  <div class="abs info" style="left:492px;top:27px">
    <svg width="28" height="28" viewBox="0 0 28 28"><circle cx="14" cy="14" r="11" fill="none" stroke="#29a3dc" stroke-width="2"/><path d="M14 8v6l4 3" fill="none" stroke="#29a3dc" stroke-width="2" stroke-linecap="round"/></svg>
    <div><strong>Mon - Fri: 9:00 - 17:30</strong>Decisions within 24 hours</div>
  </div>
  <div class="abs info" style="left:742px;top:27px">
    <svg width="24" height="28" viewBox="0 0 24 28"><path d="M12 2a8 8 0 0 0-8 8c0 6 8 15 8 15s8-9 8-15a8 8 0 0 0-8-8z" fill="none" stroke="#29a3dc" stroke-width="2"/><circle cx="12" cy="10" r="3" fill="none" stroke="#29a3dc" stroke-width="2"/></svg>
    <div><strong>42 Wharf Road</strong>Leeds, LS1 4BT</div>
  </div>
  <div class="abs info" style="left:960px;top:27px">
    <svg width="26" height="28" viewBox="0 0 26 28"><path d="M6 3l5 1 2 6-3 2c1 3 4 6 7 7l2-3 6 2 1 5c-1 2-3 3-5 3C11 25 2 16 2 6c0-2 2-3 4-3z" fill="none" stroke="#29a3dc" stroke-width="2" stroke-linejoin="round"/></svg>
    <div><strong>(0113) 4960 218</strong>info@herontrade.example</div>
  </div>
</header>

<nav class="abs mainnav">
  <ul>
    <li class="active">Home</li>
    <li>About Us <svg width="8" height="5" viewBox="0 0 8 5"><path d="M0 0l4 5 4-5z" fill="currentColor"/></svg></li>
    <li>Services <svg width="8" height="5" viewBox="0 0 8 5"><path d="M0 0l4 5 4-5z" fill="currentColor"/></svg></li>
    <li>Introducers</li>
    <li>Contact Us</li>
  </ul>
  <svg class="abs search" width="20" height="20" viewBox="0 0 20 20"><circle cx="8" cy="8" r="6" fill="none" stroke="#fff" stroke-width="2"/><path d="M13 13l5 5" stroke="#fff" stroke-width="2" stroke-linecap="round"/></svg>
</nav>

<section class="abs hero">
  <div class="abs hero-photo" role="img" aria-label="Small business owner in a suit at work, light grey studio backdrop"></div>
  <h1 class="abs">Talk directly to the<br>people who decide</h1>
  <a class="abs btn btn-primary learn">Apply Today</a>
  <a class="abs btn btn-outline ours">Our Services</a>
  <div class="abs slide-arrow" style="left:0"><svg width="10" height="16" viewBox="0 0 10 16"><path d="M8 2L2 8l6 6" fill="none" stroke="#fff" stroke-width="2"/></svg></div>
  <div class="abs slide-arrow" style="left:1159px"><svg width="10" height="16" viewBox="0 0 10 16"><path d="M2 2l6 6-6 6" fill="none" stroke="#fff" stroke-width="2"/></svg></div>
</section>

<section class="features">
  <div class="abs feature" style="left:74px">
    <svg width="74" height="74" viewBox="0 0 74 74" fill="none" stroke="#29a3dc" stroke-width="2"><path d="M2 14V2h12M60 2h12v12M72 60v12H60M14 72H2V60"/><circle cx="37" cy="37" r="15"/><path d="M41 31c-1-2-3-2-4-2-3 0-5 1-5 3 0 5 10 3 10 8 0 2-2 3-5 3-2 0-4-1-5-3M37 26v22"/></svg>
    <h3>Invoice Factoring</h3>
    <p>Release cash tied up in unpaid invoices while we manage your sales ledger for you.</p>
  </div>
  <div class="abs feature" style="left:341px">
    <svg width="74" height="74" viewBox="0 0 74 74" fill="none" stroke="#29a3dc" stroke-width="2"><path d="M2 14V2h12M60 2h12v12M72 60v12H60M14 72H2V60"/><circle cx="37" cy="38" r="15"/><path d="M37 30v8l6 4"/></svg>
    <h3>24 Hour Decisions</h3>
    <p>Send us your information and we guarantee a funding decision within 24 hours of receipt.</p>
  </div>
  <div class="abs feature" style="left:607px">
    <svg width="74" height="74" viewBox="0 0 74 74" fill="none" stroke="#29a3dc" stroke-width="2"><path d="M2 14V2h12M60 2h12v12M72 60v12H60M14 72H2V60"/><rect x="22" y="40" width="7" height="12"/><rect x="33" y="33" width="7" height="19"/><rect x="44" y="24" width="7" height="28"/></svg>
    <h3>Invoice Discounting</h3>
    <p>Keep control of your own credit and collections while your invoices fund steady growth.</p>
  </div>
  <div class="abs feature" style="left:876px">
    <svg width="74" height="74" viewBox="0 0 74 74" fill="none" stroke="#29a3dc" stroke-width="2"><path d="M2 14V2h12M60 2h12v12M72 60v12H60M14 72H2V60"/><rect x="20" y="28" width="34" height="24" rx="2"/><path d="M31 28v-5h12v5M20 38h34M34 36h6v5h-6z"/></svg>
    <h3>Introducers</h3>
    <p>Accountants and commercial brokers can refer clients and rely on a fast, direct answer.</p>
  </div>
</section>

<section class="abs whatwedo">
  <div class="abs bg" role="img" aria-label="Blue-tinted close-up of invoices and figures on a desk"></div>
  <h2 class="abs">What We Do</h2>
  <div class="abs rule"></div>
  <p class="abs">Invoice finance for small businesses in England and Wales</p>
  <a class="abs btn btn-primary">See All Services</a>
</section>

<section class="about">
  <h2 class="abs section-title" style="top:1292px">About Us</h2>
  <div class="abs title-rule" style="top:1356px"></div>
  <div class="abs tabs"><span>Facts</span><span>Our People</span><span>Criteria</span></div>
  <p class="abs about-intro">We are a funder, not a bank. Small business owners speak straight to the person who makes the decision, with no call centres and no waiting.</p>
  <div class="abs stats">
    <div class="stat"><b>24</b><i>Hours to a decision</i></div>
    <div class="stat"><b>5</b><i>Finance services</i></div>
    <div class="stat"><b>2</b><i>Nations covered</i></div>
  </div>
  <div class="abs about-copy">
    <h3>Friendly funding, backed by firm decisions.</h3>
    <p>Heron Trade finance is a newly established invoice finance provider for small businesses across England and Wales. We turn unpaid invoices into working capital so you can pay staff, buy stock and take on new work. Our team listens, explains every step clearly and gives you an answer within 24 hours of receiving your information.</p>
    <a class="btn">Read More</a>
  </div>
</section>

<section class="calculator">
  <div class="abs calc-band"></div>
  <div class="abs calc-photo" role="img" aria-label="Smiling business owner in a light blue shirt holding a clipboard"></div>
  <div class="abs calc-card">
    <h2>Funding Calculator</h2>
    <div class="rule"></div>
    <div class="field" style="left:48px;top:178px"><label>Invoice Value</label><div class="input"></div></div>
    <div class="field" style="left:305px;top:178px"><label>Monthly Turnover</label><div class="input"></div></div>
    <div class="field" style="left:48px;top:259px"><label>Advance Rate %</label><div class="input">85</div></div>
    <div class="field" style="left:305px;top:259px"><label>Payment Terms (days)</label><div class="input">30</div></div>
    <div class="calc-note">Results based on the data entered above</div>
    <div class="field" style="left:48px;top:402px"><label>Upfront Funding</label><div class="input"></div></div>
    <div class="field" style="left:305px;top:402px"><label>Balance on Payment</label><div class="input"></div></div>
    <div class="field total" style="left:48px;top:490px"><label>Total Available</label><div class="input"></div></div>
  </div>
</section>

<section class="testimonials">
  <h2 class="abs section-title" style="top:2502px">Testimonials</h2>
  <div class="abs title-rule" style="top:2561px"></div>
  <svg class="abs t-arrow" style="left:82px" width="18" height="34" viewBox="0 0 18 34"><path d="M16 2L2 17l14 15" fill="none" stroke="#c2c6cc" stroke-width="2"/></svg>
  <svg class="abs t-arrow" style="left:1102px" width="18" height="34" viewBox="0 0 18 34"><path d="M2 2l14 15L2 32" fill="none" stroke="#c2c6cc" stroke-width="2"/></svg>
  <div class="abs quote-card" style="left:130px">
    <div class="avatar" role="img" aria-label="Portrait of client Owen Marsh"></div>
    <p>I spoke to the decision maker on day one and had funding the next. Cash flow is no longer a worry.</p>
    <h4>Owen Marsh</h4><small>(Business Owner)</small>
  </div>
  <div class="abs quote-card" style="left:463px">
    <div class="avatar" role="img" aria-label="Portrait of client Clara Benn"></div>
    <p>I introduce clients with confidence. They get a clear answer within 24 hours, every single time.</p>
    <h4>Clara Benn</h4><small>(Accountant)</small>
  </div>
  <div class="abs quote-card" style="left:797px">
    <div class="avatar" role="img" aria-label="Portrait of client Rory Pike"></div>
    <p>Straight talking, quick decisions and a real person on the phone. A refreshing funder to work with.</p>
    <h4>Rory Pike</h4><small>(Commercial Broker)</small>
  </div>
</section>

<section class="abs partners">
  <div class="badge" style="left:146px;width:106px"><svg width="106" height="40" viewBox="0 0 106 40"><rect x="1" y="6" width="104" height="28" rx="14" fill="#c9ccd1"/></svg></div>
  <div class="badge" style="left:276px;width:110px"><svg width="110" height="50" viewBox="0 0 110 50"><circle cx="55" cy="14" r="12" fill="#c9ccd1"/><rect x="2" y="30" width="106" height="10" fill="#c9ccd1"/></svg></div>
  <div class="badge" style="left:454px;width:110px"><svg width="110" height="40" viewBox="0 0 110 40"><rect x="2" y="12" width="106" height="16" fill="#c9ccd1"/></svg></div>
  <div class="badge" style="left:631px;width:110px"><svg width="110" height="50" viewBox="0 0 110 50"><rect x="2" y="6" width="106" height="38" rx="4" fill="#c9ccd1"/></svg></div>
  <div class="badge" style="left:794px;width:120px"><svg width="120" height="54" viewBox="0 0 120 54"><path d="M60 2l58 25-58 25L2 27z" fill="#c9ccd1"/></svg></div>
  <div class="badge" style="left:979px;width:110px"><svg width="110" height="44" viewBox="0 0 110 44"><rect x="2" y="6" width="106" height="32" fill="#c9ccd1"/></svg></div>
</section>

<footer class="abs footer">
  <div class="abs brand">Heron Trade finance</div>
  <p class="abs footer-about">Invoice finance for small businesses in England and Wales, with a decision within 24 hours.</p>
  <div class="abs follow">Follow Us <i></i><i></i><i></i></div>

  <h5 class="abs" style="left:346px;top:74px">Navigation</h5>
  <div class="abs fcol-rule" style="left:346px;top:108px;width:180px"></div>
  <div class="abs links" style="left:346px;top:134px">About Us<br>Services<br>Introducers<br>Contact Us</div>
  <div class="abs links" style="left:481px;top:134px">Our People<br>Criteria<br>Apply Now</div>

  <h5 class="abs" style="left:614px;top:74px">Contact info</h5>
  <div class="abs fcol-rule" style="left:614px;top:108px;width:180px"></div>
  <div class="abs contact-icons">
    <svg width="16" height="16" viewBox="0 0 16 16"><path d="M3 1l3 1 1 3-2 1c1 2 2 3 4 4l1-2 3 1 1 3c0 1-1 2-3 2C6 14 2 10 2 4c0-2 0-3 1-3z" fill="#29a3dc"/></svg>
    <svg width="16" height="16" viewBox="0 0 16 16"><rect x="1" y="3" width="14" height="10" fill="none" stroke="#29a3dc" stroke-width="1.6"/><path d="M1 3l7 6 7-6" fill="none" stroke="#29a3dc" stroke-width="1.6"/></svg>
    <svg width="16" height="16" viewBox="0 0 16 16"><circle cx="8" cy="8" r="6.5" fill="none" stroke="#29a3dc" stroke-width="1.6"/><path d="M8 4v4l3 2" fill="none" stroke="#29a3dc" stroke-width="1.6"/></svg>
    <svg width="16" height="16" viewBox="0 0 16 16"><path d="M8 1a5 5 0 0 0-5 5c0 4 5 9 5 9s5-5 5-9a5 5 0 0 0-5-5z" fill="#29a3dc"/><circle cx="8" cy="6" r="2" fill="#333947"/></svg>
  </div>

  <div class="abs subscribe" style="left:881px;top:74px">
    <h5>Subscribe</h5>
    <div class="fcol-rule" style="width:180px;margin-top:19px"></div>
    <p style="margin-top:25px">Get funding news and updates.</p>
    <div class="sub-form"><div class="email">E-Mail</div><div class="send">Send</div></div>
  </div>
  <div class="abs bottom-rule"></div>
</footer>

</body>
</html>
```